依頼詳細
ラフではありますが、pptでチラシ案を作成しました。
要望事項も記載しておりますので、内容のご確認をお願いいたします。
不明点御座いましたら、お気軽にお申し付けください。
記載項目
記載事項もチラシ案に記載しております。
内容のご確認をお願いいたします。
不明点御座いましたら、お気軽にお申し付けください。
サイズ
A4
ページ数
両面
希望イメージ
シンプル 複雑
単色 カラフル
暗い 明るい
日常 高級
遊び心 厳粛
未来的 伝統的
女性的 男性的
希望する色
青系、無彩色系
納品ファイル
• イラストレーター形式 (.ai)
• PNG形式 (.png)
補足説明
aiとpdfでいただけますと幸いです。
ラフ案作成済です。体裁を整えていただく依頼となります。

本件のポイントを的確に捉えて表現いただいたことが決め手になりました。また、全体的なバランスと見やすさを加味して選定をさせていただだきました。

この度は、沢山の素晴らしいご提案をくださいまして、誠にありがとうございました。 素人が作成したラフ案から、こちらの意図を汲み取っていただき、どれも素晴らしい内容で、選考にはとても苦慮いたしましたが、慎重に皆様の提案を一つ一つ確認し、検討させていただきました。 お忙しい中、ご提案頂きましたこと皆様に重ねてお礼申し上げます。 次回ご提案をお願いさせていただく際もよろしくお願いいたします。

```html
<!DOCTYPE html>
<html lang="ja">
<head>
<meta charset="utf-8">
<title>RR×PPA チラシ</title>
<link href="https://fonts.googleapis.com/css2?family=Noto+Sans+JP:wght@400;500;700;900&display=swap" rel="stylesheet">
<style>
:root{
  --navy:#0b2a5c;
  --blue:#1666c0;
  --sky:#3a9be0;
  --pale:#e6f2fb;
  --yellow:#ffe94d;
  --white:#ffffff;
  --ink:#1b2233;
  --grey:#6b7382;
}
*{margin:0;padding:0;box-sizing:border-box}
html,body{width:846px;height:1200px;overflow:hidden;background:var(--white)}
body{font-family:"Noto Sans JP",sans-serif;color:var(--ink);position:relative}
.abs{position:absolute}

.header{top:14px;left:20px;right:20px;height:36px;display:flex;align-items:center}
.brand{font-size:15px;font-weight:700;color:var(--navy);display:flex;align-items:center;gap:6px}
.brand .dot{width:14px;height:14px;border-radius:50%;background:var(--sky)}
.brand .sq{width:14px;height:14px;background:var(--navy)}
.times{margin:0 12px;font-size:18px;font-weight:700;color:var(--navy)}
.badge{margin-left:auto;width:100px;height:36px;background:var(--sky);border-radius:4px}

.hero-bg{top:128px;left:0;width:846px;height:466px;
  background:linear-gradient(180deg,#ffffff 0%,#e9f4fc 30%,#bcd9f2 55%,#4c7fb8 75%,#1f3f73 100%)}

.first{top:58px;left:50%;transform:translateX(-50%);background:var(--blue);color:var(--white);
  font-weight:900;font-size:20px;padding:2px 26px;border-radius:4px;letter-spacing:1px}
.lead{top:92px;width:100%;text-align:center;font-size:29px;font-weight:900;color:var(--navy);letter-spacing:1px}
.lead:after{content:"";display:block;width:640px;height:2px;background:var(--navy);margin:4px auto 0}
.tag{top:144px;font-size:19px;font-weight:900;color:var(--blue);white-space:nowrap}
.tag.rr-tag{left:112px}
.tag.ppa-tag{left:372px}
.big{top:160px;left:96px;font-size:128px;font-weight:900;color:var(--navy);letter-spacing:-2px;line-height:1.1;white-space:nowrap}
.big .x{color:var(--blue);font-size:110px}
.big .ga{font-size:56px;margin-left:6px}
.solve{top:296px;width:100%;text-align:center;font-size:44px;font-weight:900;color:var(--navy);letter-spacing:1px}

.bubble{top:412px;left:40px;width:92px;height:92px;border-radius:50%;background:var(--blue);color:var(--white);
  font-size:13px;font-weight:700;display:flex;align-items:center;justify-content:center;text-align:center;line-height:1.4}
.cases{top:412px;left:150px;display:flex;gap:14px}
.case{width:150px}
.case .ph{height:98px;border:3px solid var(--white);background:linear-gradient(135deg,#8a6a4a,#c8a27a)}
.case:nth-child(2) .ph{background:linear-gradient(135deg,#9a4a1e,#d0703a)}
.case:nth-child(3) .ph{background:linear-gradient(135deg,#6a6f78,#aeb3ba)}
.case:nth-child(4) .ph{background:linear-gradient(135deg,#5a6068,#9aa0a8)}
.case p{margin-top:6px;background:var(--white);text-align:center;font-size:13px;font-weight:700;color:var(--navy);border-radius:2px}

.salt{top:546px;left:100px;width:646px;height:34px;background:var(--yellow);color:var(--blue);
  font-size:19px;font-weight:900;display:flex;align-items:center;justify-content:center}

.intro{top:612px;width:100%;text-align:center;font-size:17px;font-weight:700;color:var(--navy);line-height:1.6}

.scheme{top:676px;left:24px;width:798px;height:330px;background:var(--pale);border-radius:10px}
.scheme svg{position:absolute;left:0;top:0}
.operator{left:30px;top:110px;width:140px;height:140px;border-radius:50%;background:var(--white);border:3px solid var(--blue);
  display:flex;flex-direction:column;align-items:center;justify-content:center;text-align:center;gap:6px}
.operator .nm{font-size:11px;font-weight:700;color:var(--navy);line-height:1.3}
.operator .role{font-size:13px;font-weight:900;color:var(--blue)}
.bar{left:200px;top:14px;width:370px;height:30px;background:var(--blue);color:var(--white);font-size:12.5px;font-weight:700;
  display:flex;align-items:center;justify-content:center}
.step{background:var(--white);border:2px solid var(--sky);border-radius:6px;font-size:12px;line-height:1.5;padding:10px 12px 10px 60px;color:var(--ink)}
.step b{color:var(--blue)}
.num{position:absolute;left:10px;top:50%;transform:translateY(-50%);width:40px;height:40px;border-radius:50%;background:var(--sky);
  color:var(--white);font-weight:900;font-size:16px;display:flex;align-items:center;justify-content:center}
.s1{left:200px;top:62px;width:330px}
.s3{left:200px;top:222px;width:330px}
.plant{left:590px;top:20px;width:190px;height:120px;background:var(--white);border:2px solid var(--navy);border-radius:6px;text-align:center}
.plant h3,.client h3{font-size:14px;font-weight:900;color:var(--navy);padding:4px 0}
.plant .ph{margin:0 10px;height:76px;background:linear-gradient(180deg,#9fc8ec,#2e5f9c)}
.s2{left:590px;top:148px;width:190px;font-size:11px;padding:6px 8px 6px 50px;font-weight:700;color:var(--navy);border-style:dashed}
.s2 .num{width:34px;height:34px;font-size:14px;left:8px}
.client{left:590px;top:216px;width:190px;height:96px;background:var(--white);border:2px solid var(--navy);border-radius:6px;text-align:center}
.client .ph{margin:0 10px;height:54px;background:linear-gradient(180deg,#dfe6ee,#9aa8b8)}

.closing{top:1026px;width:100%;text-align:center;font-size:24px;font-weight:900;color:var(--navy)}
.closing span{background:linear-gradient(transparent 60%,var(--yellow) 60%)}
.footer{top:1080px;left:40px;right:40px;border-top:2px solid var(--navy);padding-top:10px;display:flex;align-items:center;gap:20px}
.footer .co{font-size:15px;font-weight:700;color:var(--navy);display:flex;align-items:center;gap:6px}
.footer .co .dot{width:12px;height:12px;border-radius:50%;background:var(--sky)}
.footer .info{font-size:11px;color:var(--grey);line-height:1.6}
</style>
</head>
<body>
<header class="header abs">
  <div class="brand"><span class="sq"></span>株式会社 彩光テクノロジー</div>
  <span class="times">×</span>
  <div class="brand"><span class="dot"></span>あおぞらエナジー・パートナーズ</div>
  <div class="badge" role="img" aria-label="加盟宣言バッジ"></div>
</header>

<div class="hero-bg abs" role="img" aria-label="青空の下に並ぶ屋根上の太陽光パネル"></div>
<div class="first abs">業界初！！RR×PPA</div>
<h1 class="lead abs">屋根の劣化で太陽光設置を諦めているお客様へ</h1>
<div class="tag rr-tag abs">屋根補修</div>
<div class="tag ppa-tag abs">イニシャル費ゼロの太陽光</div>
<div class="big abs">RR<span class="x">×</span>PPA<span class="ga">が</span></div>
<div class="solve abs">そんなお悩みを解決します！！</div>

<div class="bubble abs">こんな状態でも<br>お任せ下さい</div>
<div class="cases abs">
  <div class="case"><div class="ph" role="img" aria-label="塗装が剥がれた屋根"></div><p>剥がれている</p></div>
  <div class="case"><div class="ph" role="img" aria-label="錆びた屋根"></div><p>錆びている</p></div>
  <div class="case"><div class="ph" role="img" aria-label="割れや欠けのある屋根"></div><p>割れ、欠けがある</p></div>
  <div class="case"><div class="ph" role="img" aria-label="破損した屋根"></div><p>破損している</p></div>
</div>
<div class="salt abs">重塩害地域で設置が困難なお客様もご相談ください！</div>

<p class="intro abs">RR×PPAは屋根補修と太陽光発電システムを<br>組み合わせた新しいソリューションです</p>

<section class="scheme abs">
  <svg width="798" height="330" viewBox="0 0 798 330">
    <defs><marker id="ah" markerWidth="8" markerHeight="8" refX="6" refY="4" orient="auto"><path d="M0 0L8 4L0 8z" fill="#1666c0"/></marker></defs>
    <path d="M170 180 H190" stroke="#1666c0" stroke-width="3"/>
    <path d="M190 30 V262" stroke="#1666c0" stroke-width="3"/>
    <path d="M570 29 H584" stroke="#1666c0" stroke-width="3" marker-end="url(#ah)"/>
    <path d="M540 100 H584" stroke="#1666c0" stroke-width="3" marker-end="url(#ah)"/>
    <path d="M585 262 H540" stroke="#1666c0" stroke-width="3" marker-end="url(#ah)"/>
  </svg>
  <div class="operator abs"><span class="nm">あおぞらエナジー<br>パートナーズ</span><span class="role">PPA事業者</span></div>
  <div class="bar abs">屋根を補修、太陽光発電システムを設置・保守・管理</div>
  <div class="step s1 abs"><span class="num">01</span><b>お客様の初期費用はゼロ</b><br>屋根補修と発電設備の費用は当社が負担し、長期にわたり保守・管理を行います。</div>
  <div class="step s3 abs"><span class="num">03</span><b>お使い頂いた電気代を毎月お支払い</b><br>発電した電気をご使用分だけ、電力会社より安価な単価でお支払いいただきます。</div>
  <div class="plant abs"><h3>発電設備</h3><div class="ph" role="img" aria-label="屋根上の太陽光発電設備"></div></div>
  <div class="step s2 abs"><span class="num">02</span>発電した電気を供給<br>20年間、無償で保守</div>
  <div class="client abs"><h3>お客様</h3><div class="ph" role="img" aria-label="お客様の工場建屋"></div></div>
</section>

<p class="closing abs"><span>環境対策と屋根補修が一度に実現！電気代高騰の今がチャンス！！</span></p>
<footer class="footer abs">
  <div class="co"><span class="dot"></span>株式会社あおぞらエナジー・パートナーズ</div>
  <div class="info">〒100-0000 東京都千代田区青空町1-2-3 あおぞらビル5F<br>TEL 03-0000-1234　受付 9:00〜17:00（土日祝を除く）</div>
</footer>
</body>
</html>
```